Schriften der Gezeiten - Die Glockenturmfälle
Zielgruppe
Hello there, I'm a selfpublisher from germany, and i just finished a projekt. It plays 2016 in Germany, Nürnberg. And it contains all manner of typical fantasy elemants in it, but there is not one sparkling vampire. :)
Hallo erstmal, ich bin Selfpublisher und habe gerade ein Fantasy Buchprojekt beendet. Es spielt im Grunde jetzt, in Nürnberg. Es kommen allerlei typische Fantasy Elemente darin vor, was es jedoch nicht gibt sind glitzernde Vampire.
Aufgabenstellung
The Corpse of a young woman was found in an Park in Nürnberg. She was not only killed, someone took her heart and left her with Dogbitemarks, and a red cape.
Torvald is a wolfshaper, he works for the police, it is his task to find the killer.
There are all kind of fantasy persons in the story. So there is no need to put the wolf in the middle. :) I woud like to put the "Red Ridding Hood" there.
But I'm open for other suggestions.
In diesem Buch passieren ein paar wirklich ätzdende Ritualmorde, die Opfer werden alle mit einem roten Cape bedeckt oder bekleidet gefunden. Der Fall wird bearbeitet, von einem Wolfswandler in der KriPo und seiner leicht Psychopatischen "Vorgesetzten" in der Welt der Surrealen, bzw Übernatürlichen.
Was ich mir vorgestellt hatte war nicht den Wolf in den Vordergrund zu stellen, da es nicht expliziet um Werwölfe geht. Sondern viel mehr auf das Rotkäppchen einzugehen.
Das beste was mir bis jetzt einfällt wäre ein Rotkäppchen im Profil, das in der ausgestreckten Hand vor sich entweder einen Ritualdolch hält oder, dass die Hand zumindest ziehmlich Blutig wirkt und daruf ein Edelstein liegt. Das ganze im Aquarell.
Ich bin jedoch auch für komplett andere Vorschläge offen.
Wenn es noch Fragen zum Inhalt gibt könnt ihr euch gerne an mich wenden.
Ich freue mich auf die Zusammenarbeit.

```html
<!DOCTYPE html>
<html lang="de">
<head>
<meta charset="utf-8">
<title>Die Glockenturmfälle – Bea Somnitrix</title>
<link href="https://fonts.googleapis.com/css2?family=Fjalla+One&family=Poiret+One&display=swap" rel="stylesheet">
<style>
  :root {
    --page-bg: #000000;
    --text: #ffffff;
    --cover-glow: rgba(255, 255, 255, 0.6);
    --mist-light: #dcd8f0;
    --mist-mid: #9aa0c8;
    --forest-blue: #4d6d88;
    --forest-deep: #1f3447;
    --ground: #2c3346;
    --cape-red: #d83a44;
    --cover-type: #dcdde6;
    --band-line: #cfd0da;
    --portrait-leaves: #34402f;
    --portrait-hair: #c4a47c;
    --portrait-jacket: #15181b;
  }
  * { margin: 0; padding: 0; box-sizing: border-box; }
  html, body {
    width: 1200px;
    height: 848px;
    overflow: hidden;
    background: var(--page-bg);
  }
  .sheet {
    position: relative;
    width: 1200px;
    height: 848px;
    background: var(--page-bg);
    color: var(--text);
    font-family: "Fjalla One", "Arial Narrow", sans-serif;
  }

  /* Book cover */
  .book-cover {
    position: absolute;
    left: 85px;
    top: 82px;
    width: 484px;
    height: 684px;
    transform: rotate(-1.7deg);
    box-shadow: 0 0 14px 6px var(--cover-glow);
    overflow: hidden;
  }
  .cover-artwork {
    position: absolute;
    inset: 0;
    background:
      radial-gradient(ellipse 5% 9% at 24% 66%, var(--cape-red) 0%, rgba(216,58,68,0.55) 45%, rgba(216,58,68,0) 100%),
      radial-gradient(ellipse 18% 9% at 10% 60%, rgba(70,78,96,0.75) 0%, rgba(70,78,96,0) 100%),
      linear-gradient(180deg, rgba(44,51,70,0) 0%, rgba(44,51,70,0) 62%, rgba(44,51,70,0.9) 100%),
      radial-gradient(ellipse 38% 45% at 28% 42%, var(--mist-light) 0%, rgba(220,216,240,0.55) 45%, rgba(220,216,240,0) 100%),
      linear-gradient(90deg, var(--mist-mid) 0%, var(--forest-blue) 50%, var(--forest-deep) 80%, var(--forest-blue) 100%);
  }
  .cover-typography {
    position: absolute;
    inset: 0;
    width: 484px;
    height: 684px;
  }
  .cover-series, .cover-title, .cover-author {
    font-family: "Poiret One", "Futura", sans-serif;
    fill: var(--cover-type);
    stroke: var(--cover-type);
    text-transform: uppercase;
  }
  .cover-series { font-size: 21px; stroke-width: 0.9px; letter-spacing: 0.4px; }
  .cover-title { font-size: 52px; stroke-width: 2.2px; }
  .cover-author { font-size: 12px; stroke-width: 0.4px; letter-spacing: 0.6px; }
  .band-line { stroke: var(--band-line); fill: none; }

  /* Book information */
  .book-info {
    position: absolute;
    left: 656px;
    top: 104px;
    width: 465px;
  }
  .book-title {
    font-size: 38px;
    line-height: 46px;
    font-weight: 400;
    letter-spacing: -1px;
  }
  .book-author {
    font-size: 15px;
    line-height: 18px;
    margin-top: 2px;
    letter-spacing: -0.4px;
  }
  .synopsis {
    margin-top: 38px;
    font-size: 14.6px;
    line-height: 25.7px;
    text-align: justify;
    hyphens: manual;
    letter-spacing: -0.45px;
  }
  .author-bio {
    position: absolute;
    left: 656px;
    top: 532px;
    width: 211px;
    font-size: 14.6px;
    line-height: 25.6px;
    text-align: justify;
    hyphens: manual;
    letter-spacing: -0.45px;
  }
  .author-portrait {
    position: absolute;
    left: 917px;
    top: 534px;
    width: 198px;
    height: 198px;
    background:
      radial-gradient(ellipse 32% 42% at 58% 45%, var(--portrait-hair) 0%, rgba(196,164,124,0.35) 60%, rgba(196,164,124,0) 100%),
      linear-gradient(180deg, var(--portrait-leaves) 0%, var(--portrait-leaves) 55%, var(--portrait-jacket) 100%);
  }
</style>
</head>
<body>
<main class="sheet">

  <section class="book-cover">
    <div class="cover-artwork" role="img" aria-label="Nebliger, winterlicher Wald mit kahlen Bäumen; eine Gestalt im roten Umhang geht einen Waldweg entlang, links die Silhouette einer Stadt mit Kirchturm"></div>
    <svg class="cover-typography" viewBox="0 0 484 684">
      <line class="band-line" x1="44" y1="572" x2="492" y2="524" stroke-width="1.6"/>
      <line class="band-line" x1="120" y1="606" x2="470" y2="568" stroke-width="0.6" opacity="0.6"/>
      <line class="band-line" x1="10" y1="648" x2="496" y2="603" stroke-width="3.5"/>
      <text class="cover-series" x="104" y="551" transform="rotate(-5.6 104 551)" textLength="244" lengthAdjust="spacingAndGlyphs">Schriften der Gezeiten</text>
      <text class="cover-title" x="42" y="626" transform="rotate(-5.6 42 626)" textLength="408" lengthAdjust="spacingAndGlyphs">Glockenturmfälle</text>
      <text class="cover-author" x="346" y="634" transform="rotate(-5.6 346 634)" textLength="96" lengthAdjust="spacingAndGlyphs">Bea Somnitrix</text>
    </svg>
  </section>

  <section class="book-info">
    <h1 class="book-title">Die Glockenturmfälle</h1>
    <p class="book-author">von Bea Somnitrix</p>
    <p class="synopsis">Lorem ipsum dolor sit amet, consectetuer adipiscing elit. Aenean commodo ligula eget dolor. Aenean massa. Cum sociis natoque penatibus et magnis dis parturient montes, nascetur ridiculus mus. Donec quam felis, ultricies nec, pellentesque eu, pretium quis, sem. Nulla consequat massa quis enim. Donec pede justo, fringilla vel, aliquet nec, vul&shy;putate eget, arcu. In enim justo, rhoncus ut, imperdiet a, venenatis vitae, justo. Nullam dictum felis eu pede mollis pretium. Integer tincidunt. Cras dapibus. Vivamus elementum semper nisi. Aenean vulputate eleifend tellus. Aenean leo ligula, porttitor eu, consequat vitae, eleifend ac, enim. rhoncus ut, imperdiet a, venenatis vitae, justo. Nullam dictum felis eu pede mollis pretium. Integer tincidunt. Cras dapibus. Vivamus elementum sem&shy;per nisi. Aenean vulputate eleifend tellus. Aenean leo ligula, porttitor eu, consequat vitae, eleifend ac, enim.</p>
  </section>

  <p class="author-bio">per nisi. Aenean vulputate eleifend tel&shy;lus. Aenean leo ligula, porttitor eu, con&shy;sequat vitae, eleifend ac, enim. rhoncus ut, imperdiet a, venenatis vitae, justo. Nullam dictum felis eu pede mollis pre&shy;tium. Integer tincidunt. Cras dapibus. Vivamus elementum semper nisi. Ae&shy;nean vulputate eleifend tellus. Aenean</p>

  <div class="author-portrait" role="img" aria-label="Porträtfoto der Autorin vor Bäumen, mit langen blonden Locken, Sonnenbrille und dunkler Lederjacke"></div>

</main>
</body>
</html>
```